Post card selling a software for elderly visitor security

I need a postcard re-design that will entice children of elderly parents to sign-up to monitor the visitors (via online reporting dashboard) that care for them. These elderly residents live in a nursing home and many can't remember who came in the room to care for them. This is a major safety and security issue and adult children sometimes have no way of knowing who is visiting their parents. Our software provides an online reporting dashboard and sends text messages to adult children when a visitor arrives at the nursing home.

Target Market(s)

women between 50-65

Industry/Entity Type

Nursing Home

Colors

Designer to choose colors to be used in the design.

Requirements
Must have
• Must have Two questions: Are you the Primary Guardian of a resident in this community? If so, would you like to know who is visiting them?
• Must have a desktop computer and phone
• Needs to have a white background

```html
<!DOCTYPE html>
<html lang="en">
<head>
<meta charset="utf-8">
<title>Guardline Visitor Dashboard – Postcard</title>
<link rel="stylesheet" href="https://fonts.googleapis.com/css2?family=Lato:ital,wght@0,400;0,700;0,900;1,400&family=Oswald:wght@500&family=Libre+Baskerville&display=swap">
<style>
  :root{
    --paper:#f4f5f6;
    --swoosh:#a9adb3;
    --swoosh-light:#d7d9dc;
    --gold:#e3cf97;
    --ink:#2e3338;
    --accent:#1f6fb7;
    --bezel:#17181a;
    --silver:#c9ccd0;
    --screen-blue:#1d8fd6;
    --seal:#4f6f80;
    --alert-red:#e8535f;
    --alert-navy:#1d3b66;
    --row-highlight:#fbf2c9;
  }
  *{box-sizing:border-box;margin:0;padding:0}
  html,body{width:1200px;height:765px;overflow:hidden;background:#fff}
  .postcard{position:relative;width:1200px;height:765px;background:var(--paper);overflow:hidden;font-family:"Lato",sans-serif;color:var(--ink)}
  .backdrop{position:absolute;inset:0}

  .headline{position:absolute;left:62px;top:40px;width:820px}
  .headline .question{font-size:26px;font-weight:400;letter-spacing:-.2px;line-height:1.2}
  .headline .question strong{color:var(--accent);font-weight:900}
  .headline .follow-up{font-size:21px;font-style:italic;font-weight:400;margin-top:4px;line-height:1.2}

  /* desktop computer */
  .desktop{position:absolute;left:108px;top:132px;width:664px}
  .desktop .bezel{position:relative;height:412px;background:var(--bezel);border-radius:14px 14px 0 0;padding:14px}
  .desktop .screen{position:relative;width:100%;height:100%;background:linear-gradient(160deg,#43b4ef,var(--screen-blue) 55%,#0f5f9e);overflow:hidden}
  .desktop .chin{height:70px;background:linear-gradient(#dfe1e4,var(--silver));border-radius:0 0 12px 12px}
  .desktop .stand{width:150px;height:78px;margin:0 auto;background:linear-gradient(90deg,#aeb2b7,#e7e9eb 50%,#aeb2b7);clip-path:polygon(18% 0,82% 0,100% 100%,0 100%)}
  .desktop .base{width:210px;height:12px;margin:0 auto;background:#b9bdc2;border-radius:0 0 50% 50%}

  .browser{position:absolute;left:122px;top:0;right:0;bottom:68px;background:#fff;font-size:6px;color:#555}
  .browser .tabs{height:12px;background:#dee1e5;display:flex;gap:3px;padding:2px 4px 0}
  .browser .tab{background:#eef0f2;padding:1px 6px;border-radius:3px 3px 0 0}
  .browser .address{height:12px;border-bottom:1px solid #ddd;padding:2px 10px}
  .browser .address span{display:inline-block;background:#f1f3f4;border-radius:6px;padding:0 8px;width:240px}
  .app{position:absolute;top:24px;left:0;right:0;bottom:0;display:flex}
  .app .sidebar{width:16px;background:#2c3440;display:flex;flex-direction:column;align-items:center;gap:10px;padding-top:8px}
  .app .sidebar i{width:6px;height:6px;border-radius:50%;background:#7d8794}
  .app .main{flex:1;padding:8px 12px;position:relative}
  .app .title{font-family:"Libre Baskerville",serif;font-size:12px;color:#333}
  .app .subtitle{font-size:6px;color:#777;margin-bottom:8px}
  .app .section{font-size:7px;color:#444;margin:4px 0}
  .fields{display:flex;gap:10px;align-items:flex-end;margin-bottom:6px}
  .field label{display:block;font-size:5px}
  .field span{display:block;width:46px;height:8px;border:1px solid #ccc}
  .btn{display:inline-block;background:#2f7fd1;color:#fff;padding:1px 6px;border-radius:2px;font-size:5px}
  .charts{position:absolute;right:14px;top:14px;display:flex;gap:8px}
  .visits{width:100%;border-collapse:collapse;margin-top:10px;font-size:5px}
  .visits th{color:#2f7fd1;text-align:left;font-weight:400;padding:2px;border-bottom:1px solid #ddd}
  .visits td{padding:4px 2px;border-bottom:1px solid #eee}
  .visits tr.flagged td{background:var(--row-highlight)}

  .photo-popup{position:absolute;left:300px;top:262px;width:330px;height:126px;background:#fff;border:1px solid #bbb;box-shadow:0 4px 12px rgba(0,0,0,.25);padding:6px 8px}
  .photo-popup h3{font-size:9px;font-weight:400}
  .photo-popup p{font-size:5px;color:#666;margin:2px 0 6px}
  .photo-popup .photos{display:flex;gap:10px}
  .visitor-photo{flex:1;height:82px;background:linear-gradient(180deg,#e9eef2,#bcd0dc 60%,#3f86b8)}
  .pointer{position:absolute;left:248px;top:222px}

  /* trial offer */
  .trial-offer{position:absolute;left:712px;top:212px;width:170px;height:170px;border-radius:50%;background:var(--seal);color:#fff;display:flex;flex-direction:column;align-items:center;justify-content:center;text-align:center;box-shadow:0 3px 8px rgba(0,0,0,.2)}
  .trial-offer .days{font-family:"Oswald",sans-serif;font-size:26px;line-height:1.1}
  .trial-offer .offer{font-family:"Oswald",sans-serif;font-size:22px;line-height:1.2}
  .trial-offer .risk{font-family:"Oswald",sans-serif;font-size:12px;margin-top:4px;letter-spacing:.5px}

  /* phone */
  .phone{position:absolute;left:762px;top:430px;width:138px;height:284px;background:var(--bezel);border-radius:22px;padding:7px;transform:rotate(8deg)}
  .phone .display{position:relative;width:100%;height:100%;border-radius:16px;overflow:hidden;background:linear-gradient(170deg,#3a3f55,#c8445f 45%,#e46a78 60%,#2aa7a3 100%);color:#fff}
  .phone .notch{position:absolute;left:34px;top:0;width:56px;height:10px;background:var(--bezel);border-radius:0 0 8px 8px}
  .phone .clock{text-align:center;font-size:28px;font-weight:400;margin-top:22px}
  .phone .date{text-align:center;font-size:6px;margin-bottom:8px}
  .notice{margin:0 6px 5px;background:rgba(255,255,255,.55);border-radius:5px;padding:3px 5px;font-size:5px;color:#222}
  .notice b{display:block;font-size:5px;color:#444}

  .alert{position:absolute;width:88px;padding:10px 8px;border-radius:10px;border:2px solid #fff;color:#fff;font-size:11px;text-align:center;line-height:1.2;box-shadow:0 3px 6px rgba(0,0,0,.2)}
  .alert.arrival{left:872px;top:462px;background:var(--alert-red);transform:rotate(6deg)}
  .alert.departure{left:862px;top:582px;background:var(--alert-navy);transform:rotate(6deg)}
</style>
</head>
<body>
<main class="postcard">
  <svg class="backdrop" width="1200" height="765" viewBox="0 0 1200 765" aria-hidden="true">
    <path d="M700 0 H1200 V765 H1100 C1120 520 1000 200 700 0 Z" fill="var(--swoosh-light)"/>
    <path d="M820 0 H1200 V765 H1150 C1160 480 1060 180 820 0 Z" fill="var(--swoosh)"/>
    <path d="M905 0 C1080 140 1150 420 1120 765" stroke="var(--gold)" stroke-width="26" fill="none"/>
    <path d="M1000 0 H1200 V765 H1175 C1190 430 1120 170 1000 0 Z" fill="#8f949b"/>
    <path d="M0 560 C250 640 520 690 760 765 H0 Z" fill="#e4e6e8"/>
  </svg>

  <header class="headline">
    <h1 class="question">Are you the <strong>Primary Guardian</strong> of a resident in this community?</h1>
    <h2 class="follow-up">If so, would you like to know who is visiting them?</h2>
  </header>

  <section class="desktop">
    <div class="bezel">
      <div class="screen">
        <div class="browser">
          <div class="tabs"><span class="tab">Dashboard</span><span class="tab">Reports</span><span class="tab">Visitors</span><span class="tab">Settings</span></div>
          <div class="address"><span>app.guardline.example/dashboard</span></div>
          <div class="app">
            <nav class="sidebar"><i></i><i></i><i></i><i></i></nav>
            <div class="main">
              <div class="title">Guardline Visitor Dashboard</div>
              <div class="subtitle">for XYZ Senior Living</div>
              <div class="section">Search for Events</div>
              <div class="fields">
                <div class="field"><label>Starting</label><span></span></div>
                <div class="field"><label>Ending</label><span></span></div>
                <div class="field"><label>Search by</label><span></span></div>
                <div class="field"><label>Search</label><span style="width:70px"></span></div>
                <span class="btn">Submit</span>
              </div>
              <div class="section">Export Visits</div>
              <span class="btn">Export to CSV</span>
              <div class="charts">
                <svg width="30" height="30" viewBox="0 0 32 32" aria-hidden="true"><circle r="14" cx="16" cy="16" fill="#2a8fd8"/><path d="M16 16 L16 2 A14 14 0 0 1 29 20 Z" fill="#2cb3a5"/><path d="M16 16 L29 20 A14 14 0 0 1 12 30 Z" fill="#1d5c99"/></svg>
                <svg width="30" height="30" viewBox="0 0 32 32" aria-hidden="true"><circle r="11" cx="16" cy="16" fill="none" stroke="#d2447a" stroke-width="6"/><path d="M16 5 A11 11 0 0 1 27 16" fill="none" stroke="#8d4bb5" stroke-width="6"/><path d="M27 16 A11 11 0 0 1 16 27" fill="none" stroke="#f08a3c" stroke-width="6"/></svg>
              </div>
              <table class="visits">
                <tr><th>Date</th><th>Sign In</th><th>Sign Out</th><th>Resident</th><th>Visitor</th><th>Phone</th><th>Visitor Type</th><th>Resident/Staff</th></tr>
                <tr class="flagged"><td>12/31/2018</td><td>11:01 PM</td><td>—</td><td>Room 12</td><td>Sam Turner</td><td>555-0142</td><td>Nurse</td><td>Staff</td></tr>
                <tr><td>12/31/2018</td><td>7:05 PM</td><td>7:50 PM</td><td>Room 4</td><td>Family</td><td>555-0118</td><td>Guest</td><td>Resident</td></tr>
                <tr><td>12/31/2018</td><td>2:21 PM</td><td>3:02 PM</td><td>Room 9</td><td>Vendor</td><td>555-0177</td><td>Visitor</td><td>Resident</td></tr>
              </table>
            </div>
          </div>
        </div>
        <svg class="pointer" width="80" height="60" viewBox="0 0 80 60" aria-hidden="true"><path d="M6 4 L70 54" stroke="#e0302e" stroke-width="2"/><path d="M2 0 L12 4 L6 10 Z" fill="#e0302e"/></svg>
        <div class="photo-popup">
          <h3>Visitor Photos</h3>
          <p>These are photos of Sam Turner taken during a sign in on 12/31/2018 at 11:01 PM.</p>
          <div class="photos">
            <div class="visitor-photo" role="img" aria-label="Photo of a visitor in blue scrubs taken at sign in"></div>
            <div class="visitor-photo" role="img" aria-label="Second sign-in photo of the same visitor"></div>
          </div>
        </div>
      </div>
    </div>
    <div class="chin"></div>
    <div class="stand"></div>
    <div class="base"></div>
  </section>

  <div class="trial-offer" role="img" aria-label="Offer seal: 30-day free trial, no risk">
    <span class="days">30-DAY</span>
    <span class="offer">FREE TRIAL</span>
    <span class="risk">NO RISK!</span>
  </div>

  <section class="phone">
    <div class="display">
      <div class="notch"></div>
      <div class="clock">9:41</div>
      <div class="date">Monday, June 3</div>
      <div class="notice"><b>MESSAGES</b>Evan Morrow: Dr Reyes signed in at 9:02 AM</div>
      <div class="notice"><b>MESSAGES</b>Visitor left the community at 10:15 AM</div>
      <div class="notice"><b>MESSAGES</b>New visit logged for Mom today</div>
    </div>
  </section>

  <div class="alert arrival">Dr Reyes arrived to see Mom</div>
  <div class="alert departure">Dad left the community</div>
</main>
</body>
</html>
```